Website plus logo for a finance business (in Wix)

We need a revamp of our website and our logo - visit www.halvernbridging.com for the current site.

We are a relatively new finance firm, providing short term (bridging) loans to property developers and other businesses in the UK.

Most of the information will go on the homepage. The other 3 or 4 pages are relatively basic. If you felt it was appropriate, the information on page 2 (case studies) could be incorporated on page 1.

The current website isn't too bad and gives you an idea of the information we would like covering on the website and in what order.

The logo should be clean, simple and modern, probably branded around a rocket. The current logo is a good starting point. The word rocket should be the focal point though.

The main header colour scheme should be similar to the current website (deep purples) but we would consider dark blues or reds. An example of a palette of colours we really like is attached.

The style should be modern and clean. Lots of whites and background space but with an underlying warmth, suggesting trust and reliability.

Examples of good brands and websites that we like in our sector are www.brindlefunds.com, www.quarlowlending.co.uk and www.veltrope.co.uk - we particularly like Veltrope.

Important note - as part of the service, the website designer must be able to create the website in Wix once the design is approved. Our current website is through Wix and we want to keep it that way.

Therefore, once the design is approved, as part of the finalisation process, the designer will need to create the website in our existing Wix account.

This will also involve creating a mobile friendly version of the site (which is more or less automatic in Wix anyway). None of this should be difficult as Wix is very easy to use.

Thanks for your interest!

Kind regards

HalvernBridging

Target Market(s)

Small to medium property developers and businesses in the North West of the UK

Industry/Entity Type

Finance

Contact Information for Business Card

One side just feature the logo against a strong background colour.
The other side should have a nice clean look about it, with the details of our sales director, Tessa Marwick.
tessa@halvernbridging.com
0161 555 0193
07700 900418

Logo Text

Halvern Bridging

Coding

Coded - Design and coding required

Number of Pages Required

4 page

Font styles to use
Sans Serif

Colors
6b449b
0456a4

Requirements
Must have
• Clean looking home page, modelled on the examples that we've given.
• The start of the home page must make it clear what we do - this could be achieved by rotating banners.
• Must be produced in Wix once the design is approved.
• Should follow example colour palette given.
Nice to have
• Parallax pictures
Should not have
• Old fashioned or traditional styling - we do not want to look like an accountant or law firm's website

```html
<!DOCTYPE html>
<html lang="en">
<head>
<meta charset="utf-8">
<title>Halvern Bridging — Home</title>
<link href="https://fonts.googleapis.com/css2?family=Exo+2:wght@600;700&family=Open+Sans:wght@400;600&family=Rajdhani:wght@500&display=swap" rel="stylesheet">
<style>
  :root {
    --frame: #e6e6e6;
    --navy: #0a0a42;
    --brand-blue: #0a3aa8;
    --white: #ffffff;
    --panel: rgba(32, 32, 34, 0.88);
    --footer-text: #6e6e6e;
    --icon-grey: #7a7a7a;
  }
  * { box-sizing: border-box; margin: 0; padding: 0; }
  html, body { width: 1200px; height: 942px; overflow: hidden; }
  body { background: var(--frame); position: relative; font-family: "Open Sans", sans-serif; }

  .page { position: absolute; left: 14px; top: 14px; width: 1172px; height: 914px; background: var(--white); overflow: hidden; }

  .hero {
    position: absolute; left: 0; top: 0; width: 1172px; height: 877px;
    background:
      linear-gradient(180deg, var(--navy) 0%, rgba(20,24,90,0.85) 8%, rgba(60,80,150,0.35) 20%, rgba(255,255,255,0) 32%),
      linear-gradient(90deg, #8d8a84 0%, #b9c3d4 22%, #8ea7cc 40%, #c9d6e6 62%, #dfe7f0 80%, #c4d2e3 100%);
  }

  .brand { position: absolute; left: 26px; top: 40px; display: flex; align-items: center; gap: 12px; }
  .brand-dot { width: 34px; height: 34px; border-radius: 50%; background: var(--white); }
  .brand-name { font-family: "Exo 2", sans-serif; font-weight: 700; font-size: 34px; line-height: 1; color: var(--white); letter-spacing: 0.5px; }

  .main-nav { position: absolute; top: 44px; right: 13px; display: flex; height: 36px; }
  .main-nav a {
    display: flex; align-items: center; padding: 0 11px; height: 36px;
    font-family: "Exo 2", sans-serif; font-weight: 600; font-size: 13.5px;
    color: var(--white); text-decoration: none; letter-spacing: -0.2px;
  }
  .main-nav a.is-active { background: var(--brand-blue); padding: 0 14px; }

  .welcome-panel {
    position: absolute; left: 448px; top: 466px; width: 613px; height: 305px;
    background: var(--panel); border-radius: 6px; padding: 28px 29px 0 30px;
  }
  .welcome-title { font-family: "Exo 2", sans-serif; font-weight: 700; font-size: 26px; color: var(--white); letter-spacing: 0.2px; line-height: 1.2; }
  .welcome-text { margin-top: 12px; font-weight: 600; font-size: 15.4px; line-height: 21.2px; color: var(--white); }
  .btn-learn {
    display: inline-flex; align-items: center; justify-content: center;
    margin-top: 25px; width: 197px; height: 49px;
    background: var(--brand-blue); border: 1.5px solid var(--white); border-radius: 6px;
    color: var(--white); font-size: 16.5px; text-decoration: none;
  }

  .site-footer { position: absolute; left: 0; top: 877px; width: 1172px; height: 37px; display: flex; align-items: center; justify-content: space-between; padding: 0 14px 0 17px; }
  .copyright { font-family: "Rajdhani", sans-serif; font-weight: 500; font-size: 14.5px; color: var(--footer-text); }
  .social-links { display: flex; gap: 3px; }
  .social-links span { width: 21px; height: 21px; border-radius: 50%; background: var(--icon-grey); display: block; }
</style>
</head>
<body>
  <div class="page">
    <section class="hero" role="img" aria-label="Photo of two smiling businessmen in shirts and ties working at a laptop in a bright office"></section>

    <header>
      <div class="brand"><span class="brand-dot"></span><span class="brand-name">Halvern Bridging</span></div>
      <nav class="main-nav">
        <a href="#" class="is-active">HOME</a>
        <a href="#">ABOUT</a>
        <a href="#">CASE STUDIES</a>
        <a href="#">FAQS</a>
        <a href="#">INTERMEDIARIES</a>
        <a href="#">CONTACT</a>
      </nav>
    </header>

    <div class="welcome-panel">
      <h1 class="welcome-title">WELCOME TO HALVERN BRIDGING</h1>
      <p class="welcome-text">Halvern Bridging is a Manchester-based bridging loan provider, covering property purchases, developments and general business needs. We are not a broker. We fund you with our own money. When you speak to us, you speak with the decision-maker. We do not have strict lending parameters. We pride ourselves on working out an individual deal for each client. We can find solutions for most clients, large or small.</p>
      <a href="#" class="btn-learn">LEARN MORE</a>
    </div>

    <footer class="site-footer">
      <p class="copyright">© 2018 Halvern Bridging. All Rights Reserved.</p>
      <div class="social-links" aria-label="Social links"><span></span><span></span><span></span><span></span></div>
    </footer>
  </div>
</body>
</html>
```